Global Weight loss program

we need a business card based in Brooklyn , NY called ZestwellPRO . Mara Tullin Opdegard the founder and creator of ZestwellPRO Movement. A business based around nutrition, health, Whole Foods and fitness.

Industry/Entity Type

Food Service

Contact Information for Business Card

Phone number : 718-402-3859
website www.zestwellpro.example
email : mara@zestwellpro.example

Font styles to use
Sans Serif

Requirements
Must have
• logo colors
• green black and gold
Nice to have
• must be simple and sharp.
Should not have
• pictures of items

```html
<!DOCTYPE html>
<html lang="en">
<head>
<meta charset="utf-8">
<title>ZestwellPRO Business Card</title>
<link href="https://fonts.googleapis.com/css2?family=Open+Sans:wght@400;600;700&display=swap" rel="stylesheet">
<style>
  :root {
    --bg: #d2d2d2;
    --card: #0a0708;
    --gold-dark: #c29a55;
    --gold-light: #f0e6a8;
    --gold: #d8b56a;
    --white: #ffffff;
    --faint: #2a2a2a;
    --silver: #bdbdbd;
  }
  html, body {
    margin: 0;
    padding: 0;
    width: 1200px;
    height: 1008px;
    overflow: hidden;
    background: var(--bg);
    font-family: "Open Sans", sans-serif;
  }
  .canvas { position: relative; width: 1200px; height: 1008px; }
  .card {
    position: absolute;
    background: var(--card);
    overflow: hidden;
    color: var(--white);
  }
  .card--front { left: 318px; top: 166px; width: 558px; height: 319px; }
  .card--back  { left: 315px; top: 527px; width: 561px; height: 321px; }

  .brand-name {
    position: absolute;
    margin: 0;
    font-weight: 600;
    color: var(--gold);
    white-space: nowrap;
    line-height: 1;
  }
  .brand-tag {
    position: absolute;
    margin: 0;
    font-weight: 400;
    color: var(--gold-dark);
    letter-spacing: 1.4px;
    white-space: nowrap;
    line-height: 1;
  }
  .brand-square {
    position: absolute;
    background: linear-gradient(180deg, var(--gold-dark), var(--gold-light));
  }
  .faint-square {
    position: absolute;
    left: 278px; top: 12px;
    width: 270px; height: 270px;
    background: var(--faint);
    opacity: 0.55;
    border-radius: 6px;
  }

  .card--front .brand-square { left: 100px; top: 24px; width: 64px; height: 64px; }
  .card--front .brand-name { left: 52px; top: 110px; font-size: 29px; }
  .card--front .brand-tag { left: 54px; top: 143px; font-size: 8px; }

  .gold-tab {
    position: absolute;
    left: 0; top: 162px;
    width: 19px; height: 56px;
    border-radius: 0 6px 6px 0;
    background: linear-gradient(180deg, var(--gold-dark), var(--gold-light), var(--gold-dark));
  }
  .person-name {
    position: absolute; left: 54px; top: 168px; margin: 0;
    font-size: 19px; font-weight: 700; letter-spacing: 0.2px;
    text-transform: uppercase; line-height: 1;
  }
  .person-role {
    position: absolute; left: 54px; top: 195px; margin: 0;
    font-size: 15px; font-weight: 400; line-height: 1;
  }
  .divider {
    position: absolute; left: 54px; top: 225px;
    width: 451px; height: 2px; background: var(--white);
  }
  .contact {
    position: absolute; margin: 0; font-size: 15.5px; line-height: 1;
    display: flex; align-items: center; gap: 8px;
  }
  .contact svg { width: 14px; height: 14px; fill: var(--gold); }
  .contact--phone { left: 54px; top: 240px; }
  .contact--email { left: 54px; top: 264px; }
  .address {
    position: absolute; right: 53px; margin: 0;
    font-size: 15.5px; line-height: 1; text-align: right;
  }
  .address--1 { top: 240px; }
  .address--2 { top: 264px; }

  .bottom-band { position: absolute; left: 0; bottom: 0; width: 558px; height: 26px; }

  .card--back .brand-square { left: 245px; top: 80px; width: 72px; height: 72px; }
  .card--back .brand-name { left: 0; width: 561px; text-align: center; top: 192px; font-size: 38px; }
  .card--back .brand-tag { left: 0; width: 561px; text-align: center; top: 234px; font-size: 10px; }
  .website {
    position: absolute; left: 0; width: 561px; top: 278px; margin: 0;
    text-align: center; font-size: 15px; line-height: 1;
  }
  .website strong { font-weight: 700; }
</style>
</head>
<body>
<div class="canvas">

  <section class="card card--front">
    <div class="faint-square" role="img" aria-label="Faint large brand backdrop"></div>
    <div class="brand-square"></div>
    <p class="brand-name">ZestwellPRO</p>
    <p class="brand-tag">Fitness, Nutrition and Health</p>

    <div class="gold-tab"></div>
    <h1 class="person-name">Mara Tullin Opdegard</h1>
    <p class="person-role">Founder</p>
    <div class="divider"></div>

    <p class="contact contact--phone">
      <svg viewBox="0 0 24 24" aria-hidden="true"><path d="M6.6 10.8a15.1 15.1 0 0 0 6.6 6.6l2.2-2.2c.3-.3.7-.4 1-.2 1.1.4 2.3.6 3.6.6.6 0 1 .4 1 1V20c0 .6-.4 1-1 1C10.6 21 3 13.4 3 4c0-.6.4-1 1-1h3.5c.6 0 1 .4 1 1 0 1.3.2 2.5.6 3.6.1.3 0 .7-.2 1z"/></svg>
      718-402-3859
    </p>
    <p class="contact contact--email">
      <svg viewBox="0 0 24 24" aria-hidden="true"><path d="M2 5h20v14H2z M3.5 6.5 12 13l8.5-6.5" fill="var(--gold)"/><path d="M3 6l9 7 9-7" stroke="var(--card)" stroke-width="1.6" fill="none"/></svg>
      mara@zestwellpro.example
    </p>
    <p class="address address--1">Your Address Goes Here</p>
    <p class="address address--2">Address Line 2</p>

    <svg class="bottom-band" viewBox="0 0 558 26" preserveAspectRatio="none" aria-hidden="true">
      <defs>
        <linearGradient id="bandGold" x1="0" x2="1" y1="0" y2="0">
          <stop offset="0" stop-color="#c4965a"/>
          <stop offset="0.6" stop-color="#f2eeac"/>
          <stop offset="1" stop-color="#c9a25e"/>
        </linearGradient>
        <linearGradient id="bandSilver" x1="0" x2="1">
          <stop offset="0" stop-color="#8a8a8a"/>
          <stop offset="0.5" stop-color="#f4f4f4"/>
          <stop offset="1" stop-color="#9a9a9a"/>
        </linearGradient>
      </defs>
      <rect width="558" height="26" fill="#ffffff"/>
      <polygon points="0,0 350,0 333,26 0,26" fill="url(#bandGold)"/>
      <polygon points="350,0 425,0 408,26 333,26" fill="url(#bandSilver)"/>
      <g stroke="#111" stroke-width="2.5">
        <line x1="348" y1="0" x2="331" y2="26"/>
        <line x1="364" y1="0" x2="347" y2="26"/>
        <line x1="380" y1="0" x2="363" y2="26"/>
        <line x1="398" y1="0" x2="381" y2="26"/>
        <line x1="426" y1="0" x2="409" y2="26"/>
      </g>
    </svg>
  </section>

  <section class="card card--back">
    <div class="brand-square"></div>
    <p class="brand-name">ZestwellPRO</p>
    <p class="brand-tag">Fitness, Nutrition and Health</p>
    <p class="website">www.<strong>zestwellpro</strong>.example</p>
  </section>

</div>
</body>
</html>
```